BLUE HAVEN (Business Card for Training Company)

Blue Haven is a training and consultancy company with a focus on executive protection and medical. I would like the card to be nice and sharp, not overdone and in black and red. I would also like it to highlight that it is "A Dravin Company"

I would like it to be simple and highlight a few things.

1. Name
2. Title
3. Phone Number
4. Email

I would also like www.dravinholdings.example/blue-haven to be on the card somewhere.

Target Market(s)

Security Companies

Industry/Entity Type

Security

Contact Information for Business Card

Blue Haven is a training and consultancy company with a focus on executive protection and medical. I would like the card to be nice and sharp, not overdone and in black and red. I would also like it to highlight that it is "A Dravin Company" I would like it to be simple and highlight a few things. 1. Name 2. Title 3. Phone Number 4. Email I would also like www.dravinholdings.example/blue-haven to be on the card somewhere.

Requirements
Must have
• A Dravin Company listed on the card and the website
Nice to have
• Highlight Medical Training, Consultancy & Executive Protection Courses

```html
<!DOCTYPE html>
<html lang="en">
<head>
<meta charset="utf-8">
<title>Blue Haven – Business Card</title>
<link rel="stylesheet" href="https://fonts.googleapis.com/css2?family=Arimo:ital,wght@0,400;0,700;1,400&display=swap">
<style>
  :root {
    --backdrop: #2a2a2b;
    --card: #262627;
    --card-edge: #1e1e1f;
    --ink: #ffffff;
    --accent: #7d1518;
    --muted: #e6e6e6;
  }
  * { margin: 0; padding: 0; box-sizing: border-box; }
  html, body {
    width: 1200px; height: 900px; overflow: hidden;
    background: var(--backdrop);
    font-family: "Arimo", Arial, sans-serif;
    color: var(--ink);
  }
  .sheet { position: relative; width: 1200px; height: 900px; }
  .card {
    position: absolute; left: 267px; width: 666px; height: 380px;
    background: linear-gradient(100deg, var(--card-edge) 0%, var(--card) 60%, #2c2c2d 100%);
    box-shadow: 0 8px 22px rgba(0,0,0,.55);
  }
  .card--back { top: 50px; display: flex; flex-direction: column; align-items: center; justify-content: center; text-align: center; }
  .card--front { top: 470px; }

  .parent-line { font-weight: 700; font-size: 30px; letter-spacing: 1.5px; }
  .visit-line { font-weight: 700; font-size: 21px; letter-spacing: 1px; margin-top: 8px; }
  .web-line { font-weight: 700; font-size: 23px; letter-spacing: .5px; margin-top: 8px; }

  .brand {
    position: absolute; left: 52px; top: 48px;
    display: flex; align-items: center; gap: 12px;
  }
  .brand__mark { width: 18px; height: 18px; background: var(--accent); }
  .brand__name { font-weight: 700; font-size: 40px; letter-spacing: 1px; color: var(--ink); }

  .person { position: absolute; left: 44px; top: 150px; padding-left: 26px; }
  .person::before {
    content: ""; position: absolute; left: 0; top: 2px;
    width: 9px; height: 40px; background: var(--accent);
  }
  .person__name { font-size: 26px; color: var(--accent); text-transform: uppercase; }
  .person__title { font-style: italic; font-size: 16px; color: var(--muted); margin-top: 2px; }

  .contact { position: absolute; left: 52px; top: 238px; font-size: 17px; line-height: 1.35; color: var(--muted); }
  .contact__address { padding-left: 18px; }
  .contact__row { display: flex; align-items: center; gap: 10px; }
  .contact__icon { width: 14px; height: 14px; fill: var(--accent); flex: none; }
</style>
</head>
<body>
<main class="sheet">
  <section class="card card--back" aria-label="Card reverse">
    <p class="parent-line">A DRAVIN COMPANY</p>
    <p class="visit-line">VISIT NOW</p>
    <p class="web-line">www.dravinholdings.example/blue-haven</p>
  </section>

  <section class="card card--front" aria-label="Card front">
    <div class="brand">
      <span class="brand__mark"></span>
      <span class="brand__name">BLUE HAVEN</span>
    </div>

    <div class="person">
      <p class="person__name">Daniel Harlow</p>
      <p class="person__title">CEO/Founder</p>
    </div>

    <div class="contact">
      <p class="contact__address">48 Carden Avenue, Suite 210,<br>Northfield, Ohio 44067</p>
      <p class="contact__row">
        <svg class="contact__icon" viewBox="0 0 16 16" aria-hidden="true"><path d="M2 6c0-2 2-3 6-3s6 1 6 3v1h-3V6H5v1H2zM3 8h10l1 5H2z"/></svg>
        05551234987
      </p>
      <p class="contact__row">
        <svg class="contact__icon" viewBox="0 0 16 16" aria-hidden="true"><path d="M1 3h14v10H1zM2 4v1l6 4 6-4V4z"/></svg>
        info@dravinholdings.example
      </p>
    </div>
  </section>
</main>
</body>
</html>
```